We would like a business card that includes our logo on the front and the following information on the back:

Warren Pike, Owner
Phone: (555) 614-0827
email: wpikefencing@brookmail.example

Wally Pike & Sons Fencing provides the following services:
Barbed wire
Smooth wire
High tensile
Electric

On the bottom of the card please add:
Please call or email Warren for estimates.

```html
<!DOCTYPE html>
<html lang="en">
<head>
<meta charset="utf-8">
<title>Wally Pike &amp; Sons Fencing – Business Card</title>
<link rel="stylesheet" href="https://fonts.googleapis.com/css2?family=Cinzel:wght@400;600&family=Montserrat:wght@400;600;700&display=swap">
<style>
  :root {
    --bg: #e9e7e4;
    --brown: #85573a;
    --brown-deep: #6e452c;
    --ink: #2a2624;
    --white: #ffffff;
    --rule: #3a3633;
  }
  * { box-sizing: border-box; margin: 0; padding: 0; }
  html, body {
    width: 1200px; height: 939px; overflow: hidden;
    background: var(--bg);
  }
  .canvas { position: relative; width: 1200px; height: 939px; }

  .card {
    position: absolute;
    width: 560px; height: 320px;
    overflow: hidden;
    box-shadow: 0 6px 18px rgba(0,0,0,.18);
  }

  /* Front */
  .card--front {
    left: 100px; top: 100px;
    background: var(--brown);
  }
  .front-brand {
    position: absolute; left: 0; right: 0; top: 92px;
    text-align: center;
    font-family: "Cinzel", serif; font-weight: 600;
    font-size: 30px; line-height: 1.25; letter-spacing: .5px;
    color: var(--brown-deep);
  }
  .front-brand__mark {
    display: block; width: 14px; height: 14px; margin: 0 auto 14px;
    background: var(--brown-deep);
  }
  .services {
    position: absolute; left: 0; right: 0; bottom: 34px;
    text-align: center;
    font-family: "Montserrat", sans-serif; font-weight: 700;
    font-size: 14.5px; letter-spacing: 1px; color: var(--white);
  }

  /* Back */
  .card--back {
    left: 540px; top: 500px;
    background: var(--white);
  }
  .back-brand {
    position: absolute; left: 22px; top: 108px; width: 200px;
    text-align: center;
    font-family: "Cinzel", serif; font-weight: 600;
    font-size: 19px; line-height: 1.3; color: var(--ink);
  }
  .divider {
    position: absolute; left: 244px; top: 54px;
    width: 2px; height: 172px; background: var(--rule);
  }
  .divider__accent {
    position: absolute; left: -2px; top: 44px;
    width: 6px; height: 84px; background: var(--brown);
  }
  .contact {
    position: absolute; left: 270px; top: 64px;
    width: 260px;
  }
  .contact__name {
    font-family: "Cinzel", serif; font-weight: 600;
    font-size: 25px; color: var(--brown); letter-spacing: .5px;
  }
  .contact__role {
    font-family: "Montserrat", sans-serif; font-size: 13px;
    color: var(--ink); margin-top: 2px;
  }
  .contact__list { list-style: none; margin-top: 14px; }
  .contact__item {
    display: flex; align-items: center; gap: 8px;
    font-family: "Montserrat", sans-serif; font-size: 13px;
    color: var(--ink); margin-bottom: 9px; white-space: nowrap;
  }
  .contact__item svg { width: 13px; height: 13px; fill: var(--brown); flex: none; }
  .cta {
    position: absolute; left: 0; right: 0; bottom: 30px;
    text-align: center;
    font-family: "Montserrat", sans-serif; font-weight: 700;
    font-size: 15px; color: var(--brown); letter-spacing: .3px;
  }
</style>
</head>
<body>
<main class="canvas">

  <section class="card card--front" aria-label="Card front">
    <div class="front-brand">
      <span class="front-brand__mark"></span>
      Wally Pike &amp; Sons<br>Fencing
    </div>
    <p class="services">BARBED WIRE | SMOOTH WIRE | HIGH TENSILE | ELECTRIC</p>
  </section>

  <section class="card card--back" aria-label="Card back">
    <div class="back-brand">Wally Pike &amp; Sons<br>Fencing</div>

    <div class="divider"><span class="divider__accent"></span></div>

    <div class="contact">
      <h1 class="contact__name">WARREN PIKE</h1>
      <p class="contact__role">Owner</p>
      <ul class="contact__list">
        <li class="contact__item">
          <svg viewBox="0 0 24 24" aria-hidden="true"><path d="M6.6 10.8a15.1 15.1 0 0 0 6.6 6.6l2.2-2.2a1 1 0 0 1 1-.25 11.4 11.4 0 0 0 3.6.57 1 1 0 0 1 1 1V20a1 1 0 0 1-1 1A17 17 0 0 1 3 4a1 1 0 0 1 1-1h3.5a1 1 0 0 1 1 1c0 1.25.2 2.45.57 3.57a1 1 0 0 1-.25 1z"/></svg>
          (555) 614-0827
        </li>
        <li class="contact__item">
          <svg viewBox="0 0 24 24" aria-hidden="true"><path d="M2 5h20v14H2z M2 5l10 8 10-8" stroke="#fff" stroke-width="1.5"/></svg>
          wpikefencing@brookmail.example
        </li>
      </ul>
    </div>

    <p class="cta">Please call or email Warren for estimates.</p>
  </section>

</main>
</body>
</html>
```